Team Lantern - Site signage graphic

I need a large board creating to show our Blue Harbour plan.

I have added a previous version of this called Oak Ledger as well as the draft (AI) version of Team Lantern and our new PowerPoint as an example of branding .

Target Market(s)

Colleagues and visitors to site

Industry/Entity Type

Food manufacturing

Other font styles liked:
• Raleway Medium

Requirements
Must have
• Clear and all text as per AI mock up

```html
<!DOCTYPE html>
<html lang="en">
<head>
<meta charset="utf-8">
<title>Team Lantern – Blue Harbour Site Board</title>
<link href="https://fonts.googleapis.com/css2?family=Montserrat:wght@300;500;700;800;900&family=Oswald:wght@500;600;700&family=Amatic+SC:wght@700&family=Patrick+Hand&display=swap" rel="stylesheet">
<style>
  :root{
    --green:#27634a;
    --orange:#ee7a17;
    --yellow:#fde24a;
    --cream:#efece4;
    --cream-light:#f8f6f1;
    --ink:#111111;
    --white:#ffffff;
  }
  *{margin:0;padding:0;box-sizing:border-box}
  html,body{width:1200px;height:600px;overflow:hidden;background:var(--cream)}
  .board{position:relative;width:1200px;height:600px;background:var(--cream);font-family:"Montserrat",sans-serif;overflow:hidden}

  .brand-disc{position:absolute;left:-60px;top:-90px;width:255px;height:220px;border-radius:50%;background:var(--cream-light)}
  .brand{position:absolute;left:30px;top:46px;display:flex;align-items:center;gap:10px}
  .brand-dot{width:16px;height:16px;border-radius:50%;background:var(--orange)}
  .brand-name{font-weight:800;font-size:26px;line-height:1;color:var(--green);letter-spacing:.5px}

  .kicker{position:absolute;left:50px;top:148px;font-weight:700;font-size:24px;line-height:22px;color:var(--ink);text-transform:uppercase}
  .kicker-rule{position:absolute;left:330px;top:190px;width:216px;height:1.5px;background:var(--ink)}

  .big-five{position:absolute;left:26px;top:178px;font-weight:900;font-size:230px;line-height:1;color:var(--ink);letter-spacing:-6px}
  .headline-top{position:absolute;left:146px;top:196px;font-weight:800;font-size:74px;line-height:1;color:var(--green);letter-spacing:-1px}
  .headline-bottom{position:absolute;left:150px;top:274px;width:398px;font-size:49px;line-height:1;white-space:nowrap}
  .headline-bottom .light{font-weight:300;color:var(--green)}
  .headline-bottom .bold{font-weight:800;color:var(--orange);letter-spacing:-1px}

  .banner{position:absolute;left:150px;top:335px;width:396px;height:30px}
  .banner-text{position:absolute;left:150px;top:335px;width:396px;height:30px;display:flex;align-items:center;justify-content:center;font-weight:700;font-size:16px;color:var(--yellow);letter-spacing:.3px}

  .farm-scene{position:absolute;left:165px;top:390px;width:360px;height:106px;border-radius:4px;background:linear-gradient(180deg,#e4e6dc 0%,#c9d4c6 60%,#9fb8a7 100%)}

  .heritage{position:absolute;left:151px;top:506px;font-weight:500;font-size:11.5px;line-height:13px;color:#444;text-transform:uppercase}
  .heritage-rule{position:absolute;left:329px;top:503px;width:1px;height:32px;background:#777}
  .industry{position:absolute;left:339px;top:506px;font-weight:800;font-size:11.5px;line-height:13px;color:#222;text-transform:uppercase}

  .priority-panel{position:absolute;left:667px;top:0;width:533px;height:549px;background:var(--green)}

  .priority-list{position:absolute;left:600px;top:0;width:540px;height:549px;list-style:none}
  .priority{position:absolute;left:0;width:540px;height:103px;display:flex;align-items:center}
  .priority-divider{position:absolute;left:602px;width:538px;height:2px;background:var(--orange)}
  .priority-number{width:67px;font-family:"Oswald",sans-serif;font-weight:700;font-size:86px;line-height:1;color:var(--green);text-align:left}
  .priority-icon{width:66px;height:66px;border-radius:50%;background:var(--white);display:flex;align-items:center;justify-content:center;margin-left:13px;flex-shrink:0}
  .priority-icon svg{width:40px;height:40px;fill:none;stroke:var(--orange);stroke-width:2.4;stroke-linecap:round;stroke-linejoin:round}
  .priority-copy{flex:1;min-width:0;text-align:center;padding-left:8px}
  .priority-title{font-family:"Oswald",sans-serif;font-weight:600;font-size:24px;line-height:1.1;color:var(--white);text-transform:uppercase;letter-spacing:-.4px;white-space:nowrap}
  .priority-tag{font-family:"Amatic SC",sans-serif;font-weight:700;font-size:26px;line-height:1;color:var(--yellow);margin-top:5px;white-space:nowrap}

  .footer-band{position:absolute;left:0;top:549px;width:1200px;height:51px;background:var(--orange);display:flex;align-items:center;justify-content:center;gap:18px}
  .footer-line{font-weight:800;font-size:24px;color:var(--white);letter-spacing:.2px}
  .footer-sep{width:1.5px;height:26px;background:var(--yellow)}
  .footer-sign{font-family:"Patrick Hand",cursive;font-size:26px;color:#2a2a2a}
</style>
</head>
<body>
<main class="board">
  <div class="brand-disc"></div>
  <div class="brand">
    <span class="brand-name">TEAM LANTERN</span>
    <span class="brand-dot"></span>
  </div>

  <p class="kicker">From cheesemakers<br>to changemakers:</p>
  <div class="kicker-rule"></div>

  <div class="big-five">5</div>
  <div class="headline-top">PRIORITIES</div>
  <div class="headline-bottom"><span class="light">BLUE </span><span class="bold">HARBOUR</span></div>

  <svg class="banner" viewBox="0 0 396 30" preserveAspectRatio="none" aria-hidden="true">
    <polygon points="8,0 396,0 388,30 0,30" fill="var(--green)"/>
  </svg>
  <div class="banner-text">FIVE PRIORITIES. ONE FUTURE.</div>

  <div class="farm-scene" role="img" aria-label="Illustration of a dairy farm with barns, a silo, trees and grazing cows"></div>

  <p class="heritage">Proud of our heritage.<br>Focused on our future</p>
  <div class="heritage-rule"></div>
  <p class="industry">From farm to fork.<br>We're shaping the industry.</p>

  <div class="priority-panel"></div>
  <div class="priority-divider" style="top:131px"></div>
  <div class="priority-divider" style="top:233px"></div>
  <div class="priority-divider" style="top:336px"></div>
  <div class="priority-divider" style="top:439px"></div>

  <ul class="priority-list">
    <li class="priority" style="top:28px">
      <span class="priority-number">1</span>
      <span class="priority-icon"><svg viewBox="0 0 40 40"><circle cx="20" cy="9" r="4"/><circle cx="9" cy="12" r="3"/><circle cx="31" cy="12" r="3"/><path d="M13 22a7 7 0 0 1 14 0"/><path d="M4 24a5 5 0 0 1 7-5"/><path d="M36 24a5 5 0 0 0-7-5"/><path d="M20 36c0-6 4-9 10-9 0 6-4 9-10 9z"/><path d="M20 36c0-6-4-9-10-9 0 6 4 9 10 9z"/></svg></span>
      <div class="priority-copy"><div class="priority-title">People, Places &amp; Products</div><div class="priority-tag">WE DO THINGS THE RIGHT WAY</div></div>
    </li>
    <li class="priority" style="top:131px">
      <span class="priority-number">2</span>
      <span class="priority-icon"><svg viewBox="0 0 40 40"><path d="M20 3l14 5v10c0 9-6 15-14 19C12 33 6 27 6 18V8z"/><rect x="14" y="18" width="12" height="10" rx="1.5"/><path d="M16 18v-3a4 4 0 0 1 8 0v3"/><circle cx="20" cy="23" r="1.2"/></svg></span>
      <div class="priority-copy"><div class="priority-title">Cyber Security</div><div class="priority-tag">PROTECTING WHAT MATTERS</div></div>
    </li>
    <li class="priority" style="top:234px">
      <span class="priority-number">3</span>
      <span class="priority-icon"><svg viewBox="0 0 40 40"><circle cx="20" cy="16" r="11"/><circle cx="20" cy="16" r="7"/><path d="M20 12.5l1.2 2.4 2.6.4-1.9 1.8.5 2.6-2.4-1.3-2.4 1.3.5-2.6-1.9-1.8 2.6-.4z"/><path d="M13 25l-4 10 4-1 2 3 4-9"/><path d="M27 25l4 10-4-1-2 3-4-9"/></svg></span>
      <div class="priority-copy"><div class="priority-title">Quality &amp; Continuous Improvement</div><div class="priority-tag">BE THE BEST AT WHAT WE DO</div></div>
    </li>
    <li class="priority" style="top:337px">
      <span class="priority-number">4</span>
      <span class="priority-icon"><svg viewBox="0 0 40 40"><circle cx="20" cy="12" r="5"/><circle cx="9" cy="15" r="3.5"/><circle cx="31" cy="15" r="3.5"/><path d="M11 32v-3a9 9 0 0 1 18 0v3z"/><path d="M3 30v-2a6 6 0 0 1 7-6"/><path d="M37 30v-2a6 6 0 0 0-7-6"/></svg></span>
      <div class="priority-copy"><div class="priority-title">Customer Focus</div><div class="priority-tag">BUILD TRUST. CREATE VALUE. FOR THE LONG TERM.</div></div>
    </li>
    <li class="priority" style="top:440px">
      <span class="priority-number">5</span>
      <span class="priority-icon"><svg viewBox="0 0 40 40"><path d="M14 24a9 9 0 1 1 12 0c-1.5 1.5-2 3-2 5h-8c0-2-.5-3.5-2-5z"/><path d="M16 32h8M17 35h6"/><path d="M18 29v-6l2-3 2 3v6"/><path d="M20 2v3M6 8l2 2M34 8l-2 2M2 18h3M35 18h3"/></svg></span>
      <div class="priority-copy"><div class="priority-title">Transformation &amp; Innovation</div><div class="priority-tag">SHAPING TOMORROW, TODAY</div></div>
    </li>
  </ul>

  <footer class="footer-band">
    <span class="footer-line">ONE BUSINESS. ONE PURPOSE. FIVE PRIORITIES.</span>
    <span class="footer-sep"></span>
    <span class="footer-sign">Let's thrive together.</span>
  </footer>
</main>
</body>
</html>
```